Branvique needs a business Card Design

We are looking for a business card Design for our new Managed Service Provider Company, Branvique. Branvique encompasses everything IT for the average medium sized business. Our primary services are help desk support, cyber-security (malware and ransomware protection), and Disaster Recovery systems. We would like the design to have a very clean and professional look, with a very minimalist feel.

Target Market(s)

Medium to large sized businesses

Industry/Entity Type

It Service

Contact Information for Business Card

Name GoesHere
name@branvique.com
O: 555-382-6047
C: 555-731-5820

Font styles to use
Other font styles liked:
• Poppins Font Only Please

Colors

Designer to choose only greyscale colors for use in the design.

Requirements
Must have
• Logo included
Nice to have
• Cutting Edge, innovative, minimalistic, elegant

```html
<!DOCTYPE html>
<html lang="en">
<head>
<meta charset="utf-8">
<title>Branvique Business Card</title>
<link href="https://fonts.googleapis.com/css2?family=Poppins:wght@300;400;500&display=swap" rel="stylesheet">
<style>
  :root {
    --backdrop: #3e3a39;
    --card-frost: #a7a9ab;
    --card-edge: #c4c6c8;
    --ink: #1f4d69;
  }
  * { margin: 0; padding: 0; box-sizing: border-box; }
  html, body {
    width: 1200px;
    height: 800px;
    overflow: hidden;
    background: var(--backdrop);
  }
  .canvas {
    position: relative;
    width: 1200px;
    height: 800px;
    display: flex;
    align-items: center;
    justify-content: center;
  }
  .business-card {
    position: relative;
    width: 880px;
    height: 540px;
    border-radius: 36px;
    background: linear-gradient(160deg, #b1b3b5 0%, var(--card-frost) 55%, #9a9c9e 100%);
    border: 2px solid var(--card-edge);
    font-family: "Poppins", sans-serif;
    color: var(--ink);
  }
  .brand-block {
    position: absolute;
    left: 70px;
    top: 0;
    width: 320px;
    height: 100%;
    display: flex;
    align-items: center;
    justify-content: center;
  }
  .brand-name {
    font-size: 34px;
    font-weight: 300;
    letter-spacing: 0.42em;
    text-transform: uppercase;
    margin-right: -0.42em;
  }
  .divider {
    position: absolute;
    left: 405px;
    top: 150px;
    width: 40px;
    height: 250px;
  }
  .contact-block {
    position: absolute;
    left: 470px;
    top: 175px;
    line-height: 1.32;
  }
  .contact-name {
    font-size: 38px;
    font-weight: 500;
    letter-spacing: 0.02em;
    margin-bottom: 4px;
  }
  .contact-line {
    font-size: 27px;
    font-weight: 400;
  }
</style>
</head>
<body>
<main class="canvas">
  <section class="business-card">
    <div class="brand-block">
      <span class="brand-name">Branvique</span>
    </div>
    <svg class="divider" viewBox="0 0 40 250" aria-hidden="true">
      <path d="M36 0 L4 250" stroke="var(--ink)" stroke-width="3" stroke-linecap="round"/>
    </svg>
    <div class="contact-block">
      <p class="contact-name">Name GoesHere</p>
      <p class="contact-line">name@branvique.com</p>
      <p class="contact-line">O: 555-382-6047</p>
      <p class="contact-line">C: 555-731-5820</p>
    </div>
  </section>
</main>
</body>
</html>
```